Harborline Security and Surveillance Business Card

Business Card Design - Company Name:Freedom Security and SurveillanceWe are a Security Systems Integrator Specializing in Security Systems/ Video Surveillance and Access Control. Our areas of expertise are:Security SystemsVideo SurveillanceAccess ControlFire Alarm SystemsNetwork CablingCellular BoostersMy input is the Front of the Card is: logo, name of Business, My Name, Phone Number, and email.Rear of Card is the 6 areas of expertise, I just dont want the front to be very busy.
Name: Tom Werner
Title: President
Email: tom@harborlinesecsys.example
website: harborlinesecsys.example

```html
<!DOCTYPE html>
<html lang="en">
<head>
<meta charset="utf-8">
<title>Harborline Security and Surveillance – Business Card</title>
<link href="https://fonts.googleapis.com/css2?family=Montserrat:wght@400;500;600;700&display=swap" rel="stylesheet">
<style>
  :root{
    --backdrop:#737376;
    --card:#1d1d1f;
    --brand-blue:#3a73c8;
    --ink-light:#f2f2f2;
    --ink-muted:#8a8a8e;
    --rule:#d9d9d9;
  }
  *{box-sizing:border-box;margin:0;padding:0}
  html,body{width:1200px;height:950px;overflow:hidden}
  body{
    background:var(--backdrop);
    font-family:"Montserrat",Arial,sans-serif;
    display:flex;align-items:center;justify-content:center;gap:40px;
  }
  .card{
    position:relative;width:540px;height:309px;background:var(--card);
    overflow:hidden;box-shadow:0 10px 24px rgba(0,0,0,.35);
  }
  /* front */
  .brand{
    position:absolute;left:0;right:0;top:92px;
    display:flex;flex-direction:column;align-items:center;gap:14px;
  }
  .brand-mark{width:46px;height:46px;border-radius:50%;background:var(--brand-blue)}
  .brand-name{
    color:var(--brand-blue);font-weight:500;font-size:25px;letter-spacing:1.5px;
    text-transform:uppercase;line-height:1;
  }
  .brand-tagline{
    display:flex;align-items:center;gap:10px;margin-top:-6px;
    color:var(--ink-muted);font-size:9px;letter-spacing:3.5px;text-transform:uppercase;
  }
  .brand-tagline::before,.brand-tagline::after{content:"";width:70px;height:1px;background:var(--ink-muted)}
  .address-band{
    position:absolute;left:0;right:0;bottom:0;height:34px;background:var(--brand-blue);
    color:#fff;font-size:11px;display:flex;align-items:center;justify-content:center;letter-spacing:.3px;
  }
  /* back */
  .corner-brand{
    position:absolute;right:26px;top:26px;display:flex;align-items:center;gap:8px;
  }
  .corner-mark{width:20px;height:20px;border-radius:50%;background:var(--brand-blue)}
  .corner-text{display:flex;flex-direction:column;align-items:flex-start}
  .corner-name{color:var(--ink-light);font-size:14px;font-weight:500;letter-spacing:.8px;text-transform:uppercase;line-height:1.1}
  .corner-tagline{color:var(--ink-muted);font-size:6px;letter-spacing:2.4px;text-transform:uppercase;border-top:1px solid var(--ink-muted);padding-top:2px;margin-top:2px}
  .person{position:absolute;left:30px;top:112px}
  .person-name{color:var(--ink-light);font-weight:700;font-size:17px;letter-spacing:.8px;text-transform:uppercase}
  .person-rule{width:92px;height:1px;background:var(--rule);margin:6px 0 5px}
  .person-title{color:var(--ink-muted);font-size:10px}
  .contacts{position:absolute;left:30px;top:190px;list-style:none;display:flex;flex-direction:column;gap:11px}
  .contact{display:flex;align-items:center;gap:12px;color:var(--ink-light);font-size:12px}
  .contact-icon{width:20px;height:20px;flex:none}
</style>
</head>
<body>

<section class="card card-front" aria-label="Card front">
  <div class="brand">
    <span class="brand-mark" aria-hidden="true"></span>
    <span class="brand-name">Harborline Security</span>
    <span class="brand-tagline">and Surveillance</span>
  </div>
  <div class="address-band">Cedar Bend, Minnesota 55990, United States</div>
</section>

<section class="card card-back" aria-label="Card back">
  <div class="corner-brand">
    <span class="corner-mark" aria-hidden="true"></span>
    <div class="corner-text">
      <span class="corner-name">Harborline Security</span>
      <span class="corner-tagline">and Surveillance</span>
    </div>
  </div>

  <div class="person">
    <div class="person-name">Tom Werner</div>
    <div class="person-rule"></div>
    <div class="person-title">President</div>
  </div>

  <ul class="contacts">
    <li class="contact">
      <svg class="contact-icon" viewBox="0 0 20 20" aria-hidden="true">
        <circle cx="10" cy="10" r="9" fill="none" stroke="var(--brand-blue)" stroke-width="1.4"/>
        <rect x="5.5" y="7" width="9" height="6.5" rx="0.8" fill="var(--brand-blue)"/>
        <path d="M5.8 7.4 10 10.6 14.2 7.4" fill="none" stroke="var(--card)" stroke-width="0.9"/>
      </svg>
      tom@harborlinesecsys.example
    </li>
    <li class="contact">
      <svg class="contact-icon" viewBox="0 0 20 20" aria-hidden="true">
        <circle cx="10" cy="10" r="9" fill="none" stroke="var(--brand-blue)" stroke-width="1.4"/>
        <circle cx="10" cy="10" r="4.6" fill="var(--brand-blue)"/>
        <path d="M5.4 10h9.2M10 5.4c-2 2.6-2 6.6 0 9.2M10 5.4c2 2.6 2 6.6 0 9.2" fill="none" stroke="var(--card)" stroke-width="0.7"/>
      </svg>
      harborlinesecsys.example
    </li>
    <li class="contact">
      <svg class="contact-icon" viewBox="0 0 20 20" aria-hidden="true">
        <circle cx="10" cy="10" r="9" fill="none" stroke="var(--brand-blue)" stroke-width="1.4"/>
        <path d="M7 5.6l1.6 2.2-1 1.1c.6 1.4 1.6 2.4 3 3l1.1-1 2.2 1.6-.8 1.6c-3.4-.2-6.5-3.3-6.7-6.7z" fill="var(--brand-blue)"/>
      </svg>
      (555) 014-2290
    </li>
  </ul>
</section>

</body>
</html>
```